Larkmoor Health- Core Values Graphic for Visual Appeal

I would like a poster that could take these written core values from our organization and create a graphic that we could use for our staff and employees. I would also like to incorporate our branding into this project. Thank you!

Target Market(s)

To helps patients and employees understand the core values of our organization

Industry/Entity Type

Healthcare

Requirements
Must have
• Match our branding
Nice to have
• Please use your creativity!
Should not have
• Overly complex/ busy

```html
<!DOCTYPE html>
<html lang="en">
<head>
<meta charset="utf-8">
<title>Larkmoor Health – Core Values</title>
<link rel="stylesheet" href="https://fonts.googleapis.com/css2?family=Lato:wght@400;700&family=Nunito:wght@700;800&display=swap">
<style>
  :root {
    --brand-blue: #29a9e1;
    --brand-blue-dark: #1b8fc4;
    --charcoal: #3b3b3e;
    --ink: #151515;
    --text: #2c2c2c;
    --paper: #ffffff;
    --backdrop: #dcdcdc;
  }
  * { box-sizing: border-box; margin: 0; padding: 0; }
  html, body { width: 1200px; height: 1200px; overflow: hidden; }
  body {
    background: var(--backdrop);
    font-family: "Lato", Arial, sans-serif;
    color: var(--text);
    position: relative;
  }
  .poster {
    position: absolute;
    left: 220px; top: 108px;
    width: 760px; height: 984px;
    background: var(--paper);
    overflow: hidden;
  }
  .poster-art { position: absolute; inset: 0; }
  .team-photo {
    position: absolute;
    left: 233px; top: 31px;
    width: 527px; height: 200px;
    background: linear-gradient(180deg, #5bbde8 0%, #3a3a3c 55%, #1e1e20 100%);
  }
  .brand-badge {
    position: absolute;
    left: 22px; top: -24px;
    width: 208px; height: 208px;
    border-radius: 50%;
    background: var(--ink);
    display: flex; align-items: center; justify-content: center;
    text-align: center;
  }
  .brand-name {
    font-family: "Nunito", Arial, sans-serif;
    font-weight: 800;
    font-size: 30px;
    line-height: 1.05;
    color: var(--paper);
  }
  .value-text {
    position: absolute;
    font-size: 12.6px;
    line-height: 1.32;
    text-align: justify;
    color: var(--text);
  }
  .value-family { left: 457px; top: 306px; width: 268px; }
  .value-excellence { left: 24px; top: 636px; width: 258px; }
  .value-integrity { left: 457px; top: 636px; width: 278px; }
  .vision-text {
    position: absolute;
    left: 100px; top: 864px; width: 560px;
    font-size: 12.6px; line-height: 1.3;
    text-align: center;
  }
  .site-link {
    position: absolute;
    left: 202px; top: 942px;
    width: 355px; height: 60px;
    border-radius: 30px;
    background: var(--brand-blue);
    color: var(--paper);
    font-family: "Nunito", Arial, sans-serif;
    font-weight: 800;
    font-size: 21px;
    text-align: center;
    padding-top: 10px;
  }
  .icon-credit {
    position: absolute;
    left: 12px; top: 962px;
    font-size: 9px;
    color: var(--text);
  }
  .value-label {
    font-family: "Nunito", Arial, sans-serif;
    font-weight: 800;
    font-size: 25px;
    fill: var(--brand-blue);
  }
  .core-title {
    font-family: "Lato", Arial, sans-serif;
    font-weight: 700;
    font-size: 25px;
    fill: var(--paper);
  }
</style>
</head>
<body>
<main class="poster">
  <svg class="poster-art" width="760" height="984" viewBox="0 0 760 984">
    <defs>
      <path id="arc-family" d="M292 331 A80 80 0 0 1 452 331"/>
      <path id="arc-excellence" d="M193 625 A83 83 0 0 1 193 459"/>
      <path id="arc-integrity" d="M553 459 A83 83 0 0 1 553 625"/>
      <path id="arc-service" d="M274 747 A98 98 0 0 0 470 747"/>
    </defs>
    <!-- header -->
    <rect class="header-band" x="0" y="0" width="760" height="360" fill="var(--brand-blue)"/>
    <rect class="header-dark-band" x="300" y="200" width="460" height="90" fill="var(--ink)"/>
    <ellipse class="body-sheet" cx="380" cy="640" rx="640" ry="426" fill="var(--paper)"/>

    <!-- connectors -->
    <rect x="193" y="512" width="360" height="60" fill="var(--charcoal)"/>
    <rect x="342" y="557" width="60" height="190" fill="var(--charcoal)"/>
    <circle cx="373" cy="557" r="76" fill="var(--charcoal)"/>
    <circle cx="193" cy="542" r="68" fill="var(--charcoal)"/>
    <circle cx="553" cy="542" r="68" fill="var(--charcoal)"/>
    <circle cx="372" cy="747" r="68" fill="var(--charcoal)"/>
    <circle cx="193" cy="542" r="50" fill="var(--ink)"/>
    <circle cx="553" cy="542" r="50" fill="var(--ink)"/>
    <circle cx="372" cy="747" r="50" fill="var(--ink)"/>

    <!-- dotted links -->
    <g stroke="var(--brand-blue)" stroke-width="4" stroke-linecap="round" stroke-dasharray="0 8" fill="none">
      <line x1="247" y1="542" x2="300" y2="542"/>
      <line x1="446" y1="542" x2="499" y2="542"/>
      <line x1="372" y1="404" x2="372" y2="494"/>
      <line x1="372" y1="622" x2="372" y2="694"/>
    </g>

    <!-- family node -->
    <circle cx="372" cy="331" r="70" fill="var(--brand-blue)"/>
    <circle cx="372" cy="331" r="62" fill="var(--paper)"/>
    <circle cx="372" cy="331" r="56" fill="var(--brand-blue)"/>
    <g class="icon-family" fill="var(--ink)">
      <path d="M372 372 L342 342 A17 17 0 0 1 372 318 A17 17 0 0 1 402 342 Z"/>
      <circle cx="355" cy="310" r="7"/>
      <circle cx="389" cy="310" r="7"/>
    </g>
    <circle cx="372" cy="335" r="6" fill="var(--brand-blue)"/>

    <!-- excellence star -->
    <path class="icon-star" fill="var(--brand-blue)" d="M193 518 L200 534 L217 535 L204 546 L208 563 L193 554 L178 563 L182 546 L169 535 L186 534 Z"/>
    <g stroke="var(--paper)" stroke-width="3" stroke-linecap="round">
      <line x1="193" y1="505" x2="193" y2="511"/>
      <line x1="162" y1="530" x2="167" y2="532"/>
      <line x1="224" y1="530" x2="219" y2="532"/>
    </g>

    <!-- integrity heart -->
    <path class="icon-heart" fill="var(--brand-blue)" d="M553 572 L525 544 A16 16 0 0 1 553 520 A16 16 0 0 1 581 544 Z"/>
    <path d="M534 545 L560 545 L572 555" stroke="var(--paper)" stroke-width="4" fill="none" stroke-linecap="round"/>

    <!-- service heart + plus -->
    <path class="icon-care" fill="var(--paper)" d="M372 760 L350 738 A13 13 0 0 1 372 719 A13 13 0 0 1 394 738 Z"/>
    <path d="M372 729 V747 M363 738 H381" stroke="var(--ink)" stroke-width="4"/>
    <path d="M344 745 Q344 775 372 778 Q400 775 400 745" stroke="var(--brand-blue)" stroke-width="6" fill="none" stroke-linecap="round"/>

    <text class="core-title" x="373" y="551" text-anchor="middle">CORE</text>
    <text class="core-title" x="373" y="580" text-anchor="middle">VALUES</text>

    <text class="value-label"><textPath href="#arc-family" startOffset="50%" text-anchor="middle">family</textPath></text>
    <text class="value-label"><textPath href="#arc-excellence" startOffset="50%" text-anchor="middle">excellence</textPath></text>
    <text class="value-label"><textPath href="#arc-integrity" startOffset="50%" text-anchor="middle">integrity</textPath></text>
    <text class="value-label"><textPath href="#arc-service" startOffset="50%" text-anchor="middle">service</textPath></text>
  </svg>

  <div class="team-photo" role="img" aria-label="Group photo of the Larkmoor Health care team in dark branded polo shirts"></div>

  <div class="brand-badge"><span class="brand-name">Larkmoor<br>Health</span></div>

  <p class="value-text value-family">At the heart of our mission is the commitment to provide high-quality, affordable healthcare in a comforting and uplifting family-oriented environment. Just as our community is our extended family, every patient is a cherished member of our healthcare family. We treat each individual with the same care, compassion, and respect we would offer to our own loved ones.</p>

  <p class="value-text value-excellence">In line with our goal, we aspire not only to alleviate pain but also to inspire patients to become active participants in their well-being. We believe in empowering our patients through education and compassion. Our pursuit of excellence is unwavering, driven by our dedication to continuously improve our services at every level, ensuring that our community receives nothing less than exceptional care.</p>

  <p class="value-text value-integrity">In our healthcare team, 'Integrity' is non-negotiable. Our purpose is deeply rooted in ethics, integrity, and professional standards. We operate with the utmost integrity in every aspect of our work, adhering to the highest ethical principles. We understand that trust is the foundation of healthcare, and we are committed to maintaining the trust our community places in us.</p>

  <p class="vision-text">Our vision is grounded in the belief that every person possesses the innate potential for true health. We aim to facilitate the body's natural healing response by providing the highest level of service. Our hope for each patient extends beyond healing; we aspire to help you fulfill your life's mission and purpose abundantly, supporting you in your journey to well-being.</p>

  <p class="icon-credit">Icons by Pixelwell from Iconharbor.com</p>
  <p class="site-link">www.larkmoorchiro.com</p>
</main>
</body>
</html>
```